Web Design Wecangrowbright

Overview: To develop web site with 1 main page and 1 sample inside page. Site already exists, but has been put offline. Content has been fully rewritten. If I like your style, I will pay extra for additional inside pages.
WHO I AM?
www.wecangrowbright.org was originally created to become an online community for people to use my online tools, researches, and findings to learn how to become happier.
Today, my primary services is “health coaching and lifestyle specialist.” I’m a food specialist suggesting customized solutions for my clients to eat better, how to eat, cook, groceries shop, lose weight, reduce craving, and reverse diseases.
My edge is when a suggest food I explain Why such food hurts them (or make them sick –or reason of diseases) or how the food I suggest can heal them, strengthen them, or make them lose weight. My connection to food is medical and directly impacts my client’s health.
I want to be seen as a professional in clinical nutrition and as a guru in overall wellbeing.
I coach my clients’ lifestyle as a WHOLE, introducing them to new food, fitness, and teaching them techniques to better cope with life. I study their overall health, history, and treatments, diseases, allergies as a WHOLE, connecting all medical specialties.
My services:
I sell coaching sessions, for 1 hour, 2/month for a total program of 6 months. During the sessions, I not only coach client on nutrition, but also on career, relationship, fitness, goals, and the reasons why people can’t achieve their dreams, or how to remove stress or re-organize their lives.
Future services: I may want to sell products such as T-shirts and other promotional items
Payment methods: Since I sell, I’ll need paypal and credit card payment on line. I accept checks as well (they can find my address on “contact us”)
More services, near future:
As a Certified personal fitness Trainer, I will soon offer circuit training (outdoors) and boot camps in the neighborhood to get people moving, at very affordable prices. The goal of those events will be to grow my wecangrowbright community and get new clients for Health coaching.
Knowledgeable about controlling the mind, anger, and stress, I will soon offer group meditations and breathing sessions .
Objectives:
The goal of the site are:
• To entice visitors to become my clients. The look of the site needs to reflect my customized services.
• To offer to spend an hour with client for a free health history.
• To post videos about cooking videos, discussing a theme (sugar craving, which Carbs is good for me?)
• After I meet people and give them my business cards, as they visit my site, they needs to feel impressed by the caliber of expertise.
Schedules and Budget:
Target due date is 1 week from submission of my project. During that phase, I’d like to see a wireframe, colors, styles, incorporating my logo, suggesting pictures. I would like designed tabs, access to videos, and photo library.
Motivations for people to become CLIENTS:
I think what would make people want to get my services is if they see me as an expert in holistic weight loss, someone that they can share their life, thrust, and speak at length without being judged. Visuals are crucial to simply explain effect of food on the body (needs videos main page and archive videos on various topics)
Overall, the emotions we can play with - (key words) feeling energized, feeling strong, in control of your life, a holitistic approach to a new healthy lifestyle, Balance mind, fitness, and diet, take responsibility for your own life, feeling lighter, happier, more peaceful.
Key issues of my clients:
Weight issues, high blood pressure, depression, anxiety, stress, don’t know and what to cook, suffer from diabetes, celiac, digestive diseases. People are fatigued or can’t sleep. They are addicted to sugar, coffee, fast food, speedy life.
Another issue is finding time to eat better, making exercise a routine, making the time to remove stress and enjoy life.
How do I solve clients’ problems?:
Rather than being treated by various medical specialists, I look over their Overall health since childhood. I try to find triggers of their sicknesses that often originate from their lifestyle (stress, lack of exercise, eating junk, allergies) and I recommend life modification, introduce new food, exercise , and help them shuffle their lives around. My approach is extremely customized and always requires Hours of research on my side to fully guide a client.
Demographics:
Teenagers, singles, families, young mothers. Most of clients come with weight issues, some may come to reduce cravings.
Key Messages:
The main page (please find attached “wireframe”) shall give the visitor a sense he found the guru in holistic health. Whatever medical concern they have or struggle will finally be taken care of. Someone loves them and truly cares. Food knowledge is medical, flavor, and based on client’s own taste and willingness to try. The overall feel needs to be sleek and professional.
Call to Action
Ideally, I want people to e-mail me their filled up health history (can download blank men or women health history form) so I can schedule an appointment with them (the best solution for me)
People can also call me. Since calling me is for general questions about my program, I would prefer the e-mail version whereby clients send me their health history.
Creative Considerations
Layout – considerations in accordance to brand guidelines
Need suggetions!
Tone –
Expert in clinical food and holistic health.
Visual
Color palette : I’m not sure, but the background could be light gray (clinical health), golden desert, sahara desert, earthy, pottery (well being) warm colors (orange to warm brown) or other suggestion?
Photography: I thought about flash picture. 1 picture as banner with a message on it. About 3 pictures rotate randomly.
Picture A: is “holistic food, green vegetables, natural edible roots, or cruciferous vegetables, a platter of fresh fruits and vegies, or fresh market (spices, roots, fruits and vegies). Picture needs to be crisp clear.
Picture B: Ideally: a lady fitness trainer training group exercise outdoors, in a park, or a group of people exercising outside, people look happy, boot camp training, circuit training as a group
Picture C: a picture representing the soul ,meditation, a person relaxing next to beach or in forest, next to flowers or lushy plants, a person re-energizing.
Logo: attached as separate files with various backgrounds
Icons: may look cool to use vegies or weight, happy face, or ginger root…
typography, graphics: need suggestions!

Resources
• I have an existing website name “wecangrowbright.org” the site has been put out of internet since we were trying to change it. Let me know if you need to access site. Content of the site is ineffective.
• All content has been written. You can suggest layouts and tabs
Updates

Target Market(s)

My industry is Health care, holistic Health (no medications, no supplements, no surgeries)
Buyer’s Type could be anyone wanting to lose weight, feel better, reduce stress, learn to eat, to cook, to groceries shop. My buyers are confused about all diets.My audience is people WHO WANT change in their lives. Some people know they should eat better, they mostly need support and motivation.
Typical buyer is someone who wants a new chance, a new life!
My primary target buyer is:
1. Family. I wish to coach the entire family into healthier eating and teach them how to cook and eat as a family by changing their habits.
My secondary markets are:
1.Teenagers (often eating emotionally and confused about diets)

Industry/Entity Type

Requirements
Must have
• • Format – web, print, video, sound
I would like videos (youtube connect) – facebook connect – calendar (I will update) – I will update my content, videos, and photo library regularly – people should be able to e-mail me from site – maybe be able to go through web conference. 2 different words or pdf forms shall be available for download or online filling, then they should be able to e-mail forms through site or through their personal mail system. They can also print and mail it to me.
Managing the site:
I would like to upload videos, pictures and text freely and easily. I would like to manage and update content
Nice to have
• would look cool to use entire background as a super picture!

```html
<!DOCTYPE html>
<html lang="en">
<head>
<meta charset="utf-8">
<title>Wecangrowbright — Balanced Nutrition, Mind and Fitness</title>
<link rel="stylesheet" href="https://fonts.googleapis.com/css2?family=Open+Sans:wght@300;400;700&family=Noto+Serif:wght@400;700&family=Tinos:ital,wght@0,400;0,700;1,400&display=swap">
<style>
:root{
  --page:#f0f0e8;
  --panel:#fafaf6;
  --panel-line:#e2e2da;
  --green:#5aa61e;
  --green-bright:#6cb51c;
  --orange:#f7860f;
  --ink:#1b1b1b;
  --text:#333;
  --field:#9c9c9c;
  --ribbon:#b5371c;
}
*{box-sizing:border-box;margin:0;padding:0}
html,body{width:1200px;height:1200px;overflow:hidden;background:var(--page)}
body{position:relative;font-family:"Tinos",serif;color:var(--text)}
.hero{position:absolute;left:0;top:0;width:1200px;height:670px}
.hero svg{position:absolute;left:0;top:0}
.hero-title{position:absolute;left:50px;top:28px;font-family:"Open Sans",sans-serif;font-weight:300;font-size:43px;line-height:44px;color:#fff;letter-spacing:-.5px}
.slide-item{position:absolute;font-family:"Tinos",serif;font-style:italic;font-size:12px;line-height:14px;color:#7a7a7a}
.brand{position:absolute;left:898px;top:46px;display:flex;align-items:center;gap:8px}
.brand-dot{width:52px;height:52px;border-radius:50%;background:var(--green)}
.brand-name{font-family:"Noto Serif",serif;font-weight:400;font-size:22px;color:#3d3d3d}
.video-thumb{position:absolute;left:910px;top:113px;width:238px;height:141px;border-radius:12px;background:linear-gradient(180deg,#7cb8d8 0%,#dfeef2 45%,#5a8fa8 62%,#2e5c70 100%)}
.play{position:absolute;left:84px;top:30px;width:78px;height:78px;border-radius:50%;background:rgba(90,90,90,.55)}
.play::after{content:"";position:absolute;left:30px;top:22px;border-left:26px solid rgba(220,220,220,.8);border-top:17px solid transparent;border-bottom:17px solid transparent}

.content{position:absolute;left:200px;top:676px;width:800px;height:492px;background:var(--panel);border-radius:8px}
.card{position:absolute;background:#fbfbf8;border:1px solid var(--panel-line);border-radius:8px;overflow:hidden}
.about{left:12px;top:10px;width:364px;height:315px;padding:8px 16px 0 18px}
.heading{font-family:"Noto Serif",serif;font-weight:700;font-size:25px;line-height:34px;color:var(--ink);letter-spacing:-.5px}
.heading .accent{color:var(--green)}
.small{font-size:8px;line-height:16.4px;color:var(--text)}
.about-text{margin-top:4px}
.what{margin-top:10px}
.what-body{display:flex;gap:14px;margin-top:0}
.smiley{flex:none;width:76px;height:76px;border-radius:50%;background:radial-gradient(circle at 40% 35%,#fff3a0,#f6c21b 60%,#d88a07);margin-top:8px;margin-left:4px}
.testimonials{left:386px;top:10px;width:197px;height:315px;padding:6px 20px 0 24px}
.testimonials h2{font-family:"Tinos",serif;font-weight:400;font-size:21px;line-height:26px;color:#333}
.quote{font-size:11px;line-height:18px;color:var(--text);margin-top:6px}
.author{text-align:right;font-size:11px;line-height:16px;color:var(--green);margin-top:2px;margin-right:12px}
.quote.second{margin-top:12px}
.download{left:592px;top:10px;width:198px;height:150px}
.download .line{position:absolute;font-family:"Open Sans",sans-serif;font-weight:300;font-size:31px;color:var(--green-bright);line-height:1}
.newsletter{left:592px;top:174px;width:198px;height:150px}
.newsletter h2{position:absolute;left:20px;top:12px;font-family:"Open Sans",sans-serif;font-weight:300;font-size:22px;line-height:30px;color:#777;white-space:nowrap}
.field{position:absolute;left:22px;width:161px;height:31px;background:var(--field);border:1px solid #b5b5b5;font-family:"Open Sans",sans-serif;font-size:12px;color:#d0d0d0;padding:7px 10px}
.signup{position:absolute;left:117px;top:120px;width:65px;height:18px;background:#e4e4e0;font-family:"Open Sans",sans-serif;font-size:10.5px;color:#fff;text-align:center;line-height:18px}
.ribbon{position:absolute;right:-30px;top:18px;width:120px;height:22px;background:var(--ribbon);transform:rotate(45deg);font-family:"Open Sans",sans-serif;font-weight:700;font-size:11px;color:#fff;text-align:center;line-height:22px}
.quick{left:12px;top:334px;width:775px;height:148px;padding:6px 18px}
.links{position:absolute;left:9px;top:46px;display:grid;grid-template-columns:repeat(3,248px);gap:8px 7px}
.link{position:relative;height:42px;border:1px solid #dcdcd4;border-radius:8px;background:#fff;font-family:"Tinos",serif;font-weight:700;font-size:15.5px;color:#111;display:flex;align-items:center;justify-content:center;padding-left:30px}
.link .ico{position:absolute;left:10px;top:4px;width:34px;height:34px}
</style>
</head>
<body>
<header class="hero">
  <svg width="1200" height="670" viewBox="0 0 1200 670">
    <defs>
      <linearGradient id="photoTone" x1="0" y1="0" x2="1" y2="1">
        <stop offset="0" stop-color="#c9b49a"/>
        <stop offset=".35" stop-color="#b99c83"/>
        <stop offset=".6" stop-color="#8aa37a"/>
        <stop offset="1" stop-color="#3d4c6e"/>
      </linearGradient>
    </defs>
    <path d="M0,0 L690,0 C720,0 750,10 780,30 C850,80 840,150 860,200 C900,280 1000,290 1045,292 C1090,340 1090,470 1062,540 C1040,590 980,606 900,602 C820,598 720,574 640,546 C580,525 520,498 458,476 C400,455 330,404 250,412 C170,420 80,466 0,466 Z" fill="url(#photoTone)" role="img" aria-label="Photo of a smiling family sharing a healthy dinner at the kitchen table"/>
    <path transform="translate(4,10)" d="M-20,466 L0,466 C80,466 170,420 250,412 C330,404 400,455 458,476 C520,498 580,525 640,546 C720,574 820,598 900,602 C980,606 1040,590 1062,540 C1090,470 1090,340 1045,292" fill="none" stroke="var(--green-bright)" stroke-width="22"/>
    <path d="M-20,466 L0,466 C80,466 170,420 250,412 C330,404 400,455 458,476 C520,498 580,525 640,546 C720,574 820,598 900,602 C980,606 1040,590 1062,540 C1090,470 1090,340 1045,292 C1000,290 900,280 860,200 C840,150 850,80 780,30 C750,10 720,0 690,-10" fill="none" stroke="var(--orange)" stroke-width="22"/>
    <g fill="#fff" stroke="var(--orange)" stroke-width="2.5">
      <circle cx="458" cy="486" r="5.5" fill="var(--green)" stroke="var(--green)"/>
      <circle cx="498" cy="502" r="5.5"/>
      <circle cx="538" cy="520" r="5.5"/>
      <circle cx="580" cy="538" r="5.5"/>
      <circle cx="624" cy="554" r="5.5"/>
    </g>
  </svg>
  <h1 class="hero-title">ENJOY LIFE<br>TO THE FULLEST!</h1>
  <span class="slide-item" style="left:411px;top:479px">Item 1</span>
  <span class="slide-item" style="left:451px;top:496px">Item 2</span>
  <span class="slide-item" style="left:490px;top:514px">Item 3</span>
  <span class="slide-item" style="left:533px;top:532px">Item 4</span>
  <span class="slide-item" style="left:577px;top:548px">Item 5</span>
  <div class="brand"><span class="brand-dot"></span><span class="brand-name">Wecangrowbright</span></div>
  <div class="video-thumb" role="img" aria-label="Video still of a person with open arms on a sunny beach"><span class="play"></span></div>
</header>

<main class="content">
  <section class="card about">
    <h2 class="heading">About <span class="accent">Us</span></h2>
    <p class="small about-text">Lorem ipsum dolor sit amet, consectetur adipiscing elit. Nam in risus at neque fermentum ultricies quis vitae orci. Suspendisse gravida rhoncus mi, vehicula sollicitudin augue venenatis ac. Duis vulputate metus at ligula fermentum facilisis. Pellentesque accumsan eleifend lectus at lobortis. Mauris vel dui lacus. Maecenas ultricies tellus tellus. Etiam ac arcu enim, vitae commodo quam. Duis a tellus eget dui scelerisque fringilla. Vestibulum eu massa dui.</p>
    <h2 class="heading what"><span class="accent">What</span> We Do</h2>
    <div class="what-body">
      <div class="smiley" role="img" aria-label="Happy smiley icon"></div>
      <p class="small">Lorem ipsum dolor sit amet, consectetur adipiscing elit. Nam in risus at neque fermentum ultricies quis vitae orci. Suspendisse gravida rhoncus mi, vehicula sollicitudin augue venenatis ac. Duis vulputate metus at ligula fermentum facilisis. Pellentesque accumsan eleifend lectus at lobortis. Mauris vel dui</p>
    </div>
    <p class="small">Sed diamaccusantium doloremque laudantium, totam rem aperiam ipsum eaquep. Store veritatis et quenemo enim ipsam voluptatem, quia voluptas sit, aspernatur.</p>
  </section>

  <section class="card testimonials">
    <h2>Testimonials</h2>
    <p class="quote">Lorem ipsum dolor sit<br>amet, consectetur adipi-<br>scing elit. Nam in risus at<br>neque fermentum ultricies<br>quis vitae orci. Suspendisse<br>gravida rhoncus mi.</p>
    <p class="author">John Doe</p>
    <p class="quote second">Lorem ipsum dolor sit<br>amet, consectetur adipi-<br>scing elit. Nam in risus at<br>neque fermentum ultricies<br>quis vitae orci. Suspendisse<br>gravida rhoncus mi.</p>
    <p class="author">John Doe</p>
  </section>

  <section class="card download">
    <span class="line" style="left:11px;top:18px">DOWNLOAD</span>
    <svg style="position:absolute;left:8px;top:60px" width="64" height="60" viewBox="0 0 64 60" aria-hidden="true">
      <defs><radialGradient id="heartTone" cx=".35" cy=".3" r=".8"><stop offset="0" stop-color="#ff7a6e"/><stop offset=".6" stop-color="#e0161b"/><stop offset="1" stop-color="#a30d10"/></radialGradient></defs>
      <path d="M32,58 C18,46 2,34 2,18 C2,8 10,2 18,2 C25,2 30,6 32,11 C34,6 39,2 46,2 C54,2 62,8 62,18 C62,34 46,46 32,58 Z" fill="url(#heartTone)"/>
    </svg>
    <span class="line" style="left:75px;top:56px">HEALTH</span>
    <span class="line" style="left:77px;top:95px">FORMS</span>
  </section>

  <section class="card newsletter">
    <h2>Our Newsletter</h2>
    <div class="field" style="top:46px">Your Name ...</div>
    <div class="field" style="top:86px">Your Email ...</div>
    <div class="signup">SIGN UP</div>
    <div class="ribbon">SIGN UP!</div>
  </section>

  <section class="card quick">
    <h2 class="heading"><span class="accent">Quick</span> Links</h2>
    <nav class="links">
      <a class="link"><span class="ico" role="img" aria-label="Body workout figure icon" style="background:#d8d8d0;border-radius:4px"></span>BODY WORKOUT</a>
      <a class="link"><span class="ico" role="img" aria-label="Mind workout icon" style="background:radial-gradient(circle,#555 0,#222 60%,#111 62%,#fff 66%,#111 70%);border-radius:50%"></span>MIND WORKOUT</a>
      <a class="link"><svg class="ico" viewBox="0 0 34 34" aria-hidden="true"><rect x="2" y="6" width="28" height="22" rx="2" fill="#bfe3f5" stroke="#6aa9cc"/><path d="M6 13h18M6 18h18M6 23h12" stroke="#6aa9cc"/><path d="M14 24 L30 4 L33 7 L17 27 L13 28 Z" fill="#f4c430" stroke="#b8860b"/></svg>BLOG</a>
      <a class="link"><svg class="ico" viewBox="0 0 34 34" aria-hidden="true"><rect x="2" y="4" width="30" height="27" rx="2" fill="#fff" stroke="#bbb"/><rect x="2" y="4" width="30" height="7" fill="#e0672a"/><g fill="#ccc"><rect x="6" y="14" width="4" height="3"/><rect x="12" y="14" width="4" height="3"/><rect x="18" y="14" width="4" height="3"/><rect x="24" y="14" width="4" height="3"/><rect x="6" y="20" width="4" height="3"/><rect x="12" y="20" width="4" height="3"/><rect x="18" y="20" width="4" height="3"/><rect x="24" y="20" width="4" height="3"/></g></svg>CALENDAR</a>
      <a class="link"><svg class="ico" viewBox="0 0 34 34" aria-hidden="true"><circle cx="17" cy="17" r="15" fill="#1f63b8" stroke="#0d3f80"/><circle cx="17" cy="10" r="2.4" fill="#fff"/><rect x="15" y="14" width="4" height="12" fill="#fff"/></svg>ABOUT US</a>
      <a class="link"><svg class="ico" viewBox="0 0 34 34" aria-hidden="true"><rect x="1" y="7" width="32" height="21" fill="#f4f4f4" stroke="#aaa"/><path d="M1 7 L17 19 L33 7" fill="none" stroke="#aaa"/></svg>CONTACT</a>
    </nav>
  </section>
</main>
</body>
</html>
```